Wine Label named: Amber Ridge

We are a wine producer, who wishes to launch a new premium wine called: Amber Ridge
Our winery is situated in a rolling hill, with slopes, where Amber Ridge exists in the property. One dates to the 15th century and the other more recent to the 18th century. Its a unique feature of the winery and we wish to create a label that represents these, but is NOT religious! Difficult task I know. Think you can pull it off? Let us see it! We start with one label, but the winner will have 5 more labels to design.

Target Market(s)

30-50 year old men

Industry/Entity Type

Wine

Colors

Designer to choose colors to be used in the design.

Requirements
Must have
• serious look and premium feel. name of the wine: Amber Ridge
Nice to have
• 2019 14% ABV
Should not have
• a religious look and feel

```html
<!DOCTYPE html>
<html lang="en">
<head>
<meta charset="utf-8">
<title>Amber Ridge – Wine Label</title>
<link rel="stylesheet" href="https://fonts.googleapis.com/css2?family=Oranienbaum&family=Montserrat:wght@400;500&display=swap">
<style>
  :root {
    --canvas: #ffffff;
    --label-paper: #e6e6e6;
    --ink: #5f5f5f;
    --ink-soft: #8a8a8a;
  }
  html, body {
    margin: 0;
    padding: 0;
    width: 1200px;
    height: 1200px;
    overflow: hidden;
    background: var(--canvas);
  }
  .label {
    position: absolute;
    left: 312px;
    top: 118px;
    width: 576px;
    height: 964px;
    display: block;
  }
  .label-paper { fill: var(--label-paper); }
  .label-frame {
    fill: none;
    stroke: var(--ink);
    stroke-width: 1.1;
  }
  .wine-name {
    font-family: "Oranienbaum", "Times New Roman", serif;
    font-size: 39px;
    fill: var(--ink);
    letter-spacing: 0.3px;
  }
  .wine-type {
    font-family: "Montserrat", Arial, sans-serif;
    font-size: 7px;
    font-weight: 500;
    fill: var(--ink);
    letter-spacing: 1.6px;
  }
  .vintage {
    font-family: "Oranienbaum", "Times New Roman", serif;
    font-size: 24px;
    fill: var(--ink);
  }
  .abv {
    font-family: "Montserrat", Arial, sans-serif;
    font-size: 8px;
    fill: var(--ink);
    letter-spacing: 0.6px;
  }
</style>
</head>
<body>
<svg class="label" viewBox="0 0 312 522" xmlns="http://www.w3.org/2000/svg">
  <defs>
    <radialGradient id="estate-tone" cx="0.5" cy="0.55" r="0.6">
      <stop offset="0" stop-color="#6a6a6a" stop-opacity="0.75"/>
      <stop offset="0.6" stop-color="#7a7a7a" stop-opacity="0.45"/>
      <stop offset="1" stop-color="#8a8a8a" stop-opacity="0"/>
    </radialGradient>
    <radialGradient id="ornament-tone" cx="0.5" cy="0.5" r="0.5">
      <stop offset="0" stop-color="#5f5f5f" stop-opacity="0.55"/>
      <stop offset="0.65" stop-color="#6f6f6f" stop-opacity="0.25"/>
      <stop offset="1" stop-color="#8a8a8a" stop-opacity="0"/>
    </radialGradient>
  </defs>

  <path class="label-paper" d="M0,522 L0,190 C0,110 80,45 156,0 C232,45 312,110 312,190 L312,522 Z"/>

  <path class="label-frame" d="M19,455 L19,215 C19,140 90,88 156,62 C222,88 293,140 293,215 L293,455"/>
  <line class="label-frame" x1="74" y1="502" x2="240" y2="502"/>

  <ellipse role="img" aria-label="Ornamental filigree finial at the top of the arch"
           cx="156" cy="36" rx="50" ry="30" fill="url(#ornament-tone)"/>
  <ellipse role="img" aria-label="Ornamental filigree flourish in the lower left corner"
           cx="36" cy="482" rx="36" ry="32" fill="url(#ornament-tone)"/>
  <ellipse role="img" aria-label="Ornamental filigree flourish in the lower right corner"
           cx="276" cy="482" rx="36" ry="32" fill="url(#ornament-tone)"/>

  <ellipse role="img" aria-label="Engraved sketch of the historic estate building above rows of hillside vineyards"
           cx="157" cy="222" rx="112" ry="66" fill="url(#estate-tone)"/>

  <text class="wine-name" x="156" y="339" text-anchor="middle">AMBER RIDGE</text>
  <text class="wine-type" x="157" y="357" text-anchor="middle">PREMIUM RED WINE</text>

  <text class="vintage" x="156" y="463" text-anchor="middle">2019</text>
  <text class="abv" x="156" y="487" text-anchor="middle">14% ABV</text>
</svg>
</body>
</html>
```